Letterhead for 3 attorney Workers' Comp law firm

We are a 3 attorney law office. We specialize in Workers' Compensation. Our office represents workers who are injured on the job, and the estates of workers who are killed one the job.
When we started our office, we created our own letterhead & have been using it for years. We've just recently hired the 3rd attorney, and were going to just add his name to the letterhead, but have decided we wanted to get a professionally designed letterhead and business cards at this point.
We want something that looks clean and professional. It must look good in black and white because we often make multiple copies of our documents. We're hoping for a design that resonates confidence, reliability and experience.
The design must include the firm name: Thornbury & Calder, PLLC. We would like the PLLC to be small compared to the Thornbury & Calder graphic. We also want to incorporate the attorney names: Ivar Thornbury, Delia Calder, and Glen Rutledge. Our current letterhead has our contact info in the footer at the bottom of the page. We like that design, but are open to the idea of having it at the top. We'll leave that at the discretion of the designer. Our contact info is as follows: 482 S. Harrow Avenue, Suite 310 Bellingham, WA 98417 Phone: 360-555-2917, Fax: 360-555-4068, and our website: www.thornburycalder.example
Target Market(s)
Clients, courts, other legal offices, doctors offices. These are the people who see our letterhead most frequently. It's not so much for marketing purposes, mainly so that we have a professional image when sending out documents.
Industry/Entity Type
Law Firm
Contact Information for Business Card
On the back of the business card: it can be designed, or be a template for filling in appointment reminder information (i.e. date, time, etc)
Colors
Designer to choose colors to be used in the design.
Requirements
Must have
- Must have our firm name at the top.
- Must include the attorney names.
- Must have all of our contact information (can be at top or bottom - whatever looks best with the design)
Nice to have
- A strong, confident design
Should not have
- We don't want the design to be playful, cartoony or busy.

```html
<!DOCTYPE html>
<html lang="en">
<head>
<meta charset="utf-8">
<title>Thornbury &amp; Calder, PLLC — Letterhead and Business Cards</title>
<link rel="stylesheet" href="https://fonts.googleapis.com/css2?family=Libre+Baskerville:wght@400;700&display=swap">
<style>
  :root {
    --backdrop: #efefef;
    --paper: #ffffff;
    --ink: #111111;
    --ink-soft: #6b6b6b;
    --rule: #c9c9c9;
    --band: #000000;
    --band-text: #ffffff;
    --shadow: rgba(0, 0, 0, 0.22);
  }
  * { box-sizing: border-box; margin: 0; padding: 0; }
  html, body {
    width: 1200px; height: 1000px; overflow: hidden;
    background: var(--backdrop);
    font-family: "Libre Baskerville", Georgia, serif;
    color: var(--ink);
  }
  .stage { position: relative; width: 1200px; height: 1000px; }

  /* Letterhead */
  .letterhead {
    position: absolute; left: 57px; top: 115px;
    width: 535px; height: 758px;
    background: var(--paper);
    box-shadow: 0 3px 8px var(--shadow);
  }
  .letterhead__mast {
    position: absolute; left: 0; right: 0; top: 26px;
    text-align: center;
  }
  .wordmark {
    font-family: "Libre Baskerville", Georgia, serif;
    font-weight: 400; color: var(--ink);
    text-transform: uppercase; line-height: 0.95;
    letter-spacing: -0.5px;
  }
  .letterhead .wordmark { font-size: 30px; }
  .wordmark__suffix { font-size: 0.62em; letter-spacing: 0.5px; }
  .letterhead__rule {
    width: 224px; height: 1px; background: var(--rule);
    margin: 8px auto 6px;
  }
  .attorneys {
    font-size: 10px; color: var(--ink-soft); letter-spacing: 0.2px;
  }
  .attorneys .sep { margin: 0 6px; }
  .letterhead__footer {
    position: absolute; left: 0; right: 0; bottom: 0; height: 45px;
    background: var(--band); color: var(--band-text);
    font-size: 7.5px; text-align: center; padding-top: 11px; line-height: 13px;
  }
  .letterhead__footer .sep { margin: 0 26px; }
  .letterhead__footer b { font-weight: 700; margin-right: 4px; }

  /* Business card front */
  .card {
    position: absolute; width: 395px; height: 255px;
    box-shadow: 0 3px 8px var(--shadow);
  }
  .card--front { left: 630px; top: 265px; background: var(--paper); }
  .card__name {
    position: absolute; left: 25px; top: 38px;
    font-size: 14px; font-weight: 700; letter-spacing: 0.3px;
  }
  .card__divider {
    position: absolute; left: 224px; top: 22px;
    width: 1px; height: 48px; background: var(--ink);
  }
  .card--front .wordmark {
    position: absolute; left: 236px; top: 24px;
    font-size: 18px;
  }
  .card__address {
    position: absolute; left: 25px; top: 146px;
    font-size: 11px; line-height: 16px;
  }
  .card__contacts {
    position: absolute; left: 25px; top: 183px;
    list-style: none; font-size: 11px; line-height: 21px;
  }
  .card__contacts b { display: inline-block; width: 26px; font-weight: 700; }

  /* Business card back */
  .card--back {
    left: 745px; top: 480px;
    background: var(--band);
    border: 4px solid var(--paper);
    display: flex; align-items: center; justify-content: center;
  }
  .card--back .wordmark {
    color: var(--band-text); font-size: 24px; text-align: center;
  }
</style>
</head>
<body>
<main class="stage">

  <section class="letterhead" aria-label="Letterhead">
    <header class="letterhead__mast">
      <div class="wordmark">Thornbury<br>&amp; Calder <span class="wordmark__suffix">PLLC</span></div>
      <div class="letterhead__rule"></div>
      <p class="attorneys">Ivar Thornbury<span class="sep">|</span>Delia Calder<span class="sep">|</span>Glen Rutledge</p>
    </header>
    <footer class="letterhead__footer">
      <div><b>t</b>360-555-2917<span class="sep">|</span><b>f</b>360-555-4068<span class="sep">|</span>www.thornburycalder.example</div>
      <div>482 S. Harrow Avenue, Suite 310 Bellingham, WA 98417</div>
    </footer>
  </section>

  <section class="card card--front" aria-label="Business card front">
    <p class="card__name">Ivar Thornbury</p>
    <div class="card__divider"></div>
    <div class="wordmark">Thornbury<br>&amp; Calder <span class="wordmark__suffix">PLLC</span></div>
    <p class="card__address">482 S. Harrow Avenue,<br>Suite 310 Bellingham, WA 98417</p>
    <ul class="card__contacts">
      <li><b>t</b>360-555-2917</li>
      <li><b>f</b>360-555-4068</li>
      <li><b>w</b>www.thornburycalder.example</li>
    </ul>
  </section>

  <section class="card card--back" aria-label="Business card back">
    <div class="wordmark">Thornbury<br>&amp; Calder</div>
  </section>

</main>
</body>
</html>
```